Mexican Restaurant needs a new Menu Design

Mexican restaurant LA TORTUGA VERDE is renewing its menu, so we need something new.
Since our inception we have given the task of rescuing ingredients, recipes, and traditional and representatives dishes of the culinary techniques of yesteryear.
We are the only restaurant in Guadalajara that manufactures its own dairy natural as fresh cheese, the cream and our already well-known and traditional jocoqui. In addition, we produce organic ranch egg and are currently in the development of organic vegetables cultivated on the slopes of the old Hill which gives our plants benefit from an exceptional microclimate.
Find more information about the restaurant in www.latortugaverde.com.
The menu needs to have the full list of products with the prices, some phrases that speak of the philosophy of the ranch-style-living, photos.
We need the cover, back cover and interiors.
Updates
Thank you so much for the proposals you have submitted for the menu design. We are looking them carefully.
Thank you very much for taking your time to design a proposal for our menu!!!
Target Market(s)
The target is very wide (28-40 yrs.): Young executives, Young families, Housewives.
Industry/Entity Type
Restaurant
Look and feel
Each slider illustrates characteristics of the customer's brand and the style your logo design should communicate.

```html
<!DOCTYPE html>
<html lang="en">
<head>
<meta charset="utf-8">
<title>La Tortuga Verde — Dinner Menu</title>
<link rel="stylesheet" href="https://fonts.googleapis.com/css2?family=Fjalla+One&family=Josefin+Sans:wght@700&family=Crimson+Text:wght@600&display=swap">
<style>
  :root {
    --backdrop: #d9d6d0;
    --frame-red: #c8322b;
    --paper: #f1ebe0;
    --ink: #1e1b18;
    --accent: #d2483e;
    --rule: #e07a70;
  }
  * { box-sizing: border-box; margin: 0; padding: 0; }
  html, body { width: 1200px; height: 798px; overflow: hidden; }
  body { background: var(--backdrop); display: flex; align-items: center; justify-content: center; }

  .menu-card {
    width: 580px; height: 778px;
    background: var(--frame-red);
    padding: 22px;
    box-shadow: 0 4px 14px rgba(0,0,0,.25);
  }
  .menu-sheet {
    position: relative;
    height: 100%;
    background: var(--paper);
    color: var(--ink);
    padding: 26px 34px 20px;
    text-align: center;
    overflow: hidden;
  }

  .brand-name {
    font-family: "Fjalla One", sans-serif;
    color: var(--accent);
    font-size: 15px;
    letter-spacing: 1px;
  }
  .menu-title {
    font-family: "Josefin Sans", sans-serif;
    font-size: 20px;
    letter-spacing: 7px;
    margin-top: 16px;
  }
  .title-divider {
    font-family: "Josefin Sans", sans-serif;
    color: var(--accent);
    font-size: 13px;
    letter-spacing: 3px;
    margin-top: 4px;
  }

  .section-rule { border: 0; border-top: 1px solid var(--rule); margin: 12px 0 10px; }

  .section-heading {
    font-family: "Fjalla One", sans-serif;
    font-size: 22px;
    letter-spacing: 4px;
    color: var(--paper);
    -webkit-text-stroke: 1px var(--ink);
    text-shadow: 2px 2px 0 var(--ink);
    margin-bottom: 10px;
  }

  .dish { margin-bottom: 7px; }
  .dish-name {
    font-family: "Fjalla One", sans-serif;
    font-size: 13px;
    letter-spacing: .3px;
    line-height: 1.2;
  }
  .dish-description {
    font-family: "Crimson Text", serif;
    font-size: 12.5px;
    line-height: 1.2;
  }

  .dish-columns { display: flex; gap: 26px; margin-top: 6px; }
  .dish-column { flex: 1; }

  .main-courses { position: relative; }
  .corner-steps { position: absolute; right: -34px; top: -14px; }
</style>
</head>
<body>
  <article class="menu-card">
    <div class="menu-sheet">
      <header class="menu-header">
        <p class="brand-name">LA TORTUGA VERDE</p>
        <h1 class="menu-title">DINNER MENU</h1>
        <p class="title-divider">···//···</p>
      </header>

      <hr class="section-rule">

      <section class="starters">
        <h2 class="section-heading">STARTERS &amp; SALADS</h2>

        <div class="dish">
          <p class="dish-name">COUNTRY STYLE SPREADS WITH SALAD AND GUACAMOLE</p>
          <p class="dish-description">walnuts, cheese, walnuts, cheese, walnuts, cheese, w/ walnuts, cheese &amp; walnuts, cheese</p>
        </div>
        <div class="dish">
          <p class="dish-name">COUNTRY STYLE SPREADS</p>
          <p class="dish-description">walnuts, cheese, walnuts, cheese, walnuts, cheese, w/ walnuts, cheese &amp; walnuts, cheese</p>
        </div>

        <div class="dish-columns">
          <div class="dish-column">
            <div class="dish">
              <p class="dish-name">PICANTE PLATE</p>
              <p class="dish-description">picante bread, chilli, meat &amp; armadillo</p>
            </div>
            <div class="dish">
              <p class="dish-name">PICANTE PLATE</p>
              <p class="dish-description">picante bread, chilli, meat &amp; armadillo</p>
            </div>
            <div class="dish">
              <p class="dish-name">TACO LOCO</p>
              <p class="dish-description">picante bread, chilli,</p>
            </div>
            <div class="dish">
              <p class="dish-name">PICANTE PLATE</p>
              <p class="dish-description">picante bread, chilli, meat &amp; armadillo</p>
            </div>
          </div>
          <div class="dish-column">
            <div class="dish">
              <p class="dish-name">PICANTE PLATE</p>
              <p class="dish-description">picante bread, chilli, meat &amp; armadillo</p>
            </div>
            <div class="dish">
              <p class="dish-name">PICANTE PLATE AND TACO</p>
              <p class="dish-description">picante bread, chilli, meat &amp; armadillo</p>
            </div>
            <div class="dish">
              <p class="dish-name">PICANTE PLATE</p>
              <p class="dish-description">picante bread, chilli, meat &amp; armadillo</p>
            </div>
            <div class="dish">
              <p class="dish-name">PICANTE PLATE, FUNGHI E PROSCIUTTO</p>
              <p class="dish-description">picante bread, chilli, meat &amp; armadillo</p>
            </div>
          </div>
        </div>
      </section>

      <hr class="section-rule">

      <section class="main-courses">
        <svg class="corner-steps" width="90" height="40" viewBox="0 0 90 40" aria-hidden="true">
          <polyline points="0,6 70,6 70,14 90,14" fill="none" stroke="var(--rule)" stroke-width="1"/>
          <polyline points="0,10 66,10 66,18 90,18" fill="none" stroke="var(--rule)" stroke-width="1"/>
          <polyline points="0,14 62,14 62,22 90,22" fill="none" stroke="var(--rule)" stroke-width="1"/>
        </svg>
        <h2 class="section-heading">MAIN COURSES</h2>

        <div class="dish">
          <p class="dish-name">COUNTRY STYLE SPREADS</p>
          <p class="dish-description">walnuts, cheese, walnuts, cheese, walnuts, cheese, w/ walnuts, cheese &amp; walnuts, cheese</p>
        </div>
        <div class="dish">
          <p class="dish-name">COUNTRY STYLE SPREADS</p>
          <p class="dish-description">walnuts, cheese, walnuts, cheese, walnuts, cheese, w/ walnuts, cheese &amp; walnuts, cheese</p>
        </div>
        <div class="dish">
          <p class="dish-name">COUNTRY STYLE SOUPS FOR VEGETARIANS</p>
          <p class="dish-description">walnuts, cheese, walnuts, cheese, walnuts, cheese, w/ walnuts, cheese &amp; walnuts, cheese</p>
        </div>
      </section>
    </div>
  </article>
</body>
</html>
```